Pals of Rusty Fundraiser Flyer for shelter dogs

Flyer for Fund Raiser for shelter and rescue dogsThis will be hosted by who we are calling Heroes First responders (Fire, Police, and EMS will be bartending raising money to help the shelter dogs).

I will be uploading a basic flyer I did but I don't like it, only showing for dates and words etc...

struggling to come up with something eye-catching related to the above.

We can keep the use of Heroes (spelled wrong on the flyer)but open for new ideas too and new title.

Target Market(s)

Animal lovers

Font styles to use
Serif
Sans Serif

Requirements
Must have
• the ties to first responders and dog rescue
• Must include First responder logo badges images. The image with the helping hands Maybe replace the badges with images of dogs or doggy paws something like that
• Must have a strong presence identifying and relating to first responders
• Images of first responders as well as even images of the first responder logos for fire department police department and EMS.
• The first responders are the ones hosting the event so we really want to raise them up and show their appreciation for the cause that is super important as well
• Title should read
• Guardians Guarding Mutts

```html
<!DOCTYPE html>
<html lang="en">
<head>
<meta charset="utf-8">
<title>Pals of Rusty – Guardians Guarding Mutts</title>
<link href="https://fonts.googleapis.com/css2?family=Gochi+Hand&family=Patrick+Hand&display=swap" rel="stylesheet">
<style>
  :root {
    --bg: #47b873;
    --paper: #ffffff;
    --red: #e22a12;
    --ink: #111111;
    --gold: #d9a93f;
    --bronze: #c4864a;
    --silver: #b9bcc2;
    --dog-light: #e9d3b5;
    --dog-mid: #c98a4e;
  }
  * { box-sizing: border-box; margin: 0; padding: 0; }
  html, body { width: 1200px; height: 1200px; overflow: hidden; }
  body { background: var(--bg); display: flex; align-items: center; justify-content: center; }
  .flyer {
    position: relative; width: 792px; height: 1120px;
    background: var(--paper); overflow: hidden;
    font-family: "Patrick Hand", sans-serif; color: var(--ink);
    box-shadow: 0 20px 50px rgba(0,0,0,.3);
  }
  .shapes { position: absolute; inset: 0; }
  .event-date {
    position: absolute; left: 56px; top: 52px;
    font-family: "Gochi Hand", cursive; font-size: 60px; letter-spacing: 1px;
    white-space: nowrap;
  }
  .brand {
    position: absolute; right: 40px; top: 46px; text-align: center;
    display: flex; flex-direction: column; align-items: center; gap: 6px;
  }
  .brand-mark { width: 84px; height: 84px; border-radius: 50%; background: var(--red); }
  .brand-name { font-size: 30px; color: var(--ink); line-height: 1; white-space: nowrap; }
  .brand-sub { font-size: 14px; letter-spacing: .5px; text-transform: uppercase; white-space: nowrap; }
  .dog-photo {
    position: absolute; left: 190px; top: 160px; width: 300px; height: 465px;
    background: radial-gradient(ellipse at 50% 40%, var(--dog-light) 0 35%, var(--dog-mid) 75%);
    border-radius: 46% 46% 0 0;
  }
  .event-info {
    position: absolute; left: 500px; right: 12px; top: 330px;
    color: var(--paper); text-align: center; line-height: 1; white-space: nowrap;
  }
  .event-time { font-family: "Gochi Hand", cursive; font-size: 62px; }
  .event-host { font-size: 20px; margin: 10px 0 6px; }
  .event-venue { font-family: "Gochi Hand", cursive; font-size: 50px; }
  .title {
    position: absolute; left: 0; right: 0; top: 645px; text-align: center;
    font-family: "Gochi Hand", cursive; font-size: 48px; color: var(--red);
    letter-spacing: 1px; line-height: 1; white-space: nowrap;
  }
  .blurb {
    position: absolute; left: 80px; right: 80px; top: 712px;
    text-align: center; font-size: 21px; line-height: 1.3;
  }
  .badges {
    position: absolute; left: 0; right: 0; top: 840px;
    display: flex; justify-content: center; gap: 56px;
  }
  .badge {
    width: 130px; height: 130px; border-radius: 50%;
    border: 4px solid var(--red); display: flex; align-items: center; justify-content: center;
    background: var(--paper);
  }
  .badge-shape { width: 66px; height: 84px; clip-path: polygon(50% 0, 100% 22%, 88% 78%, 50% 100%, 12% 78%, 0 22%); }
  .badge--fire .badge-shape { background: var(--bronze); }
  .badge--police .badge-shape { background: var(--silver); clip-path: polygon(50% 0, 61% 35%, 98% 35%, 68% 57%, 79% 92%, 50% 71%, 21% 92%, 32% 57%, 2% 35%, 39% 35%); width: 88px; height: 88px; }
  .badge--ems .badge-shape { background: var(--gold); }
  .footer {
    position: absolute; left: 0; right: 0; bottom: 0; height: 100px;
    display: flex; align-items: center; justify-content: center; gap: 28px;
    color: var(--paper); padding-top: 10px;
  }
  .web { display: flex; align-items: center; gap: 12px; font-size: 26px; white-space: nowrap; }
  .divider { width: 2px; height: 56px; background: var(--paper); }
  .follow { font-size: 26px; line-height: 1.1; white-space: nowrap; }
  .social { display: flex; gap: 10px; margin-top: 4px; }
  .social span { width: 22px; height: 22px; border-radius: 50%; background: var(--paper); display: block; }
</style>
</head>
<body>
  <main class="flyer">
    <svg class="shapes" viewBox="0 0 792 1120" aria-hidden="true">
      <path d="M0 305 Q396 145 792 230 L792 520 Q430 700 0 590 Z" fill="var(--red)"/>
      <path d="M0 1055 Q396 975 792 1000 L792 1120 L0 1120 Z" fill="var(--ink)"/>
    </svg>

    <div class="event-date">AUG 15, 2019</div>

    <div class="brand">
      <span class="brand-mark"></span>
      <span class="brand-name">Pals of Rusty</span>
      <span class="brand-sub">Maple County Dog Pound</span>
    </div>

    <div class="dog-photo" role="img" aria-label="Photo of a tan and white puppy looking at the viewer"></div>

    <div class="event-info">
      <div class="event-time">6-10pm</div>
      <div class="event-host">hosted at the</div>
      <div class="event-venue">harbor club</div>
    </div>

    <h1 class="title">GUARDIANS GUARDING MUTTS</h1>

    <p class="blurb">join pals of rusty for an evening of fun! come spend an evening with our celebrity bartenders and help some pups in need. Our local men and women in uniform will be pouring drinks and raising awareness of adoption.</p>

    <div class="badges">
      <div class="badge badge--fire"><span class="badge-shape" role="img" aria-label="Fire department badge"></span></div>
      <div class="badge badge--police"><span class="badge-shape" role="img" aria-label="Police badge"></span></div>
      <div class="badge badge--ems"><span class="badge-shape" role="img" aria-label="EMS badge"></span></div>
    </div>

    <footer class="footer">
      <div class="web">
        <svg width="22" height="22" viewBox="0 0 22 22" aria-hidden="true">
          <circle cx="11" cy="11" r="9" fill="none" stroke="#fff" stroke-width="1.6"/>
          <ellipse cx="11" cy="11" rx="4" ry="9" fill="none" stroke="#fff" stroke-width="1.4"/>
          <line x1="2" y1="11" x2="20" y2="11" stroke="#fff" stroke-width="1.4"/>
        </svg>
        www.palsofrustymaple.org
      </div>
      <span class="divider"></span>
      <div class="follow">
        Follow Us:
        <div class="social"><span></span><span></span><span></span><span></span></div>
      </div>
    </footer>
  </main>
</body>
</html>
```